Clean book cover design for book about writing a book

Book title: The Crossing
Subtitle: 9 Paths to Crafting a Volume that Counts
Name: Marisol T. Brenwick, The Quill Nursery

This is a book which teaches 10 steps to writing a self-help book. I'm looking for a very clean impactful cover either with no image or just a small simple image of a book, typewriter, laptop, cabin or something very simple. I am attaching the manuscript here if reading it would help you with the cover. The theme of the book is that you can write with joy and ease and your book can just flow out of you if you learn how to clear the blocks between you and your book already written. Sort of a new agey stance on book writing.

The book should generally match the branding on my website. Www.TheQuillNursery.example.

I have photos of myself attached which I'd like used for the back cover with an "about the author section of maybe 50 words.

The project is for the full back cover and spine as well as the front cover (see print Forge template attached) but to win the contest you can just design the front cover and then I'll give the winner the template for the full design with the back cover copy. Or you can design the full cover using the template and you can use Loren ipsum text if you need to.

My clients are very upmarket and the themes of my business revolve around nuturing and incubating ideas and authors. Very feminine creation energy.

For colors see The Crossing Press (CB) wax seals and the background fades. I don't want my logo on the cover but I am attaching it here so you get a feel for the branding. The logo is in the LOBSTER font and you can see how we do the grey with the rainbow shadow.

Here are some covers I like:

http://www.shopvale.example/Pen-Tome-Quick-Stage---Stage/dp/055817342Q
http://www.shopvale.example/Plotting-Your-Tale-Chart-Triumph/dp/0841739265
http://www.shopvale.example/Be-Scribe-Seeking-Voice-Guide-ebook/dp/K22R9WQ3L1
http://www.shopvale.example/Strays-Tale-Triumph-Rupert-Vanhollow/dp/0552048871
Updates

I have revised my brief to include some picture and images that will help you create the cover. I have also included some of my favorite covers to give you more of a sense of what I'm going for. And I have included the manuscript in case it would help you to skim through it in order to get a sense of the reader and the book. I think if you look at my revised brief it will make it easier to create a submission. Thanks!

Target Market(s)

Women 40-60 who run small businesses as life coaches or other healing jobs (therapy, reiki, light work) they have a spiritual/new age bent.

Industry/Entity Type

Business

Font styles to use
Serif
Other font styles liked:
• Lobster (not required... just a suggestion since it's my logo font)

Requirements
Must have
• Name and title easy to read in 1" x 1" thumb nail
Nice to have
• Fantastic type face treatment.

Match the look and feel of my website.
Should not have
• Busy images. With one simple image or just designed with colors and typeface treatment

```html
<!DOCTYPE html>
<html lang="en">
<head>
<meta charset="utf-8">
<title>The Crossing — Marisol T. Brenwick</title>
<link rel="stylesheet" href="https://fonts.googleapis.com/css2?family=Archivo:wght@800&family=Oswald:wght@600&family=Roboto+Condensed:wght@500&family=Tinos:wght@400;700&display=swap">
<style>
  :root {
    --ink: #111111;
    --band: #231f20;
    --hot-pink: #ff0a7a;
    --white: #ffffff;
    --rule: #f5a623;
    --photo-top: #b77a9e;
    --photo-mid: #cfa6a9;
    --photo-low: #e3dcc0;
    --ring-white: #ffffff;
    --ring-pink: #f0288a;
  }
  * { margin: 0; padding: 0; box-sizing: border-box; }
  html, body { width: 821px; height: 1200px; overflow: hidden; background: #fff; }
  .cover { position: relative; width: 821px; height: 1200px; overflow: hidden; }

  .cover-photo {
    position: absolute; inset: 0;
    background: linear-gradient(170deg, var(--photo-top) 0%, #c38fa8 30%, var(--photo-mid) 55%, #dccbb5 75%, var(--photo-low) 100%);
  }

  .subtitle-frame { position: absolute; inset: 0; }

  .spine-band {
    position: absolute; left: 22px; top: 0; width: 121px; height: 1200px;
    background: var(--band);
    border-right: 6px solid var(--white);
  }
  .spine-band::after {
    content: ""; position: absolute; right: -12px; top: 0; width: 2px; height: 100%;
    background: var(--band);
  }
  .title {
    position: absolute; left: 22px; top: 40px; width: 121px; height: 1130px;
    display: flex; flex-direction: column; align-items: center;
    font-family: "Archivo", sans-serif; font-weight: 800; line-height: 1;
  }
  .title-lead { display: flex; flex-direction: column; align-items: center; color: var(--hot-pink); font-size: 74px; gap: 2px; }
  .title-main { flex: 1; display: flex; flex-direction: column; justify-content: space-between; align-items: center; color: var(--white); font-size: 92px; margin-top: 28px; }

  .subtitle { position: absolute; left: 195px; top: 420px; width: 580px; height: 300px; }
  .subtitle-number {
    position: absolute; left: 20px; top: -40px;
    font-family: "Oswald", sans-serif; font-weight: 600; font-size: 380px; line-height: 1;
    color: var(--hot-pink);
  }
  .subtitle-word {
    position: absolute; left: 290px; top: 28px;
    font-family: "Roboto Condensed", sans-serif; font-weight: 500; font-size: 66px; line-height: 1;
    letter-spacing: 9px; color: var(--hot-pink);
  }
  .subtitle-rest {
    position: absolute; left: 290px; top: 125px;
    font-family: "Roboto Condensed", sans-serif; font-weight: 500; font-size: 40px; line-height: 57px;
    color: var(--ink); text-transform: uppercase; white-space: nowrap;
  }

  .byline {
    position: absolute; left: 183px; top: 1123px;
    font-family: "Tinos", serif; font-size: 29px; color: var(--ink); white-space: nowrap;
  }
  .byline-author { font-weight: 700; margin-right: 12px; }
  .byline-imprint { font-weight: 400; }
  .byline-rule { position: absolute; left: 168px; top: 1164px; width: 632px; height: 3px; background: var(--rule); }
</style>
</head>
<body>
<div class="cover">
  <div class="cover-photo" role="img" aria-label="Soft-focus photo of a hand writing with a pen on a sheet of paper, washed in pink and pale yellow tones"></div>

  <svg class="subtitle-frame" width="821" height="1200" viewBox="0 0 821 1200" aria-hidden="true">
    <circle cx="485" cy="562" r="302" fill="#f2d8e4" fill-opacity=".35" stroke="var(--ring-white)" stroke-width="3"/>
    <circle cx="485" cy="562" r="292" fill="none" stroke="var(--ring-pink)" stroke-width="2"/>
  </svg>

  <div class="spine-band"></div>
  <h1 class="title">
    <span class="title-lead"><span>T</span><span>H</span><span>E</span></span>
    <span class="title-main"><span>C</span><span>R</span><span>O</span><span>S</span><span>S</span><span>I</span><span>N</span><span>G</span></span>
  </h1>

  <h2 class="subtitle">
    <span class="subtitle-number">9</span>
    <span class="subtitle-word">PATHS</span>
    <span class="subtitle-rest">To crafting<br>a volume that<br>counts</span>
  </h2>

  <p class="byline"><span class="byline-author">Marisol T. Brenwick</span><span class="byline-imprint">The Quill Nursery</span></p>
  <div class="byline-rule"></div>
</div>
</body>
</html>
```